Wine Label Design

We’re a wine company looking to design a new label: “Wayfarer”. The label should promote quality. I would like the label to show a compass and continents. I would like the Continents to cover the whole label and be noticable for the consumers to see. Please review the attached picture it will give you a good example of the continents design.. Also, place the compass on the top capsule and make the capsule the same dominate color as your label.

Front label dimensions: 4 H x 4 W
-Brand Name: Wayfarer
-Wine Type: Zinfandel
-Vintage: 2012
-Region: Sonoma County

Back label dimensions: 3.5 H x 3.5 W
- brand name: Wayfarers
- Vintage: 2012
- Region: Sonoma County
-Alcohol statement: Alc. 14.0% by vol. (exactly 2 mm in height)
-Volume: 750 ml (exactly 2 mm in height)

WWW.HOLBROOKWINECO.EXAMPLE (exactly 2 mm in height)

GOVERNMENT WARNING: (1) ACCORDING TO THE SURGEON GENERAL, WOMEN SHOLD NOT DRINK ALCOHOLIC BEVERAGES DURING PREGNANY BECAUSE OF THE RISK OF BIRTH DEFECTS. (2) CONSUMPTION OF ALCOHOLIC BEVERAGES IMPAIRS YOUR ABILITY TO DRIVE A CAR OR OPERATE MACHINERY, AND MAY CAUSE HEALTH PROBLEMS. (exactly 2 mm in height) (This needs to be blocked/justified format

CONTAINS SULFITES (exactly 2 mm in height)
Updates

thanks for all of your submittals.  I updated the brief for your review.

Target Market(s)

Wayfraers

Industry/Entity Type

Government

Font styles to use
Serif
Sans Serif
Decorative

Requirements
Must have
• Compass and continents

```html
<!DOCTYPE html>
<html lang="en">
<head>
<meta charset="utf-8">
<title>Wayfarers Zinfandel – Wine Labels</title>
<link rel="stylesheet" href="https://fonts.googleapis.com/css2?family=Cinzel:wght@400;700&family=Parisienne&display=swap">
<style>
  :root {
    --ink: #4a2710;
    --ink-deep: #3d1f0b;
    --paper: #ffffff;
    --trim: #e64ce6;
    --map-light: #efe3c6;
    --map-mid: #d9c49b;
    --map-dark: #b89c6c;
    --compass-rim: #5b4a36;
    --compass-face: #6e6a45;
  }
  * { box-sizing: border-box; margin: 0; padding: 0; }
  html, body { width: 1200px; height: 1000px; overflow: hidden; background: var(--paper); }
  .canvas { position: relative; width: 1200px; height: 1000px; font-family: "Cinzel", serif; color: var(--ink); }

  .label { position: absolute; background: var(--paper); border: 1px solid var(--trim); }

  /* Front label */
  .front { left: 100px; top: 238px; width: 486px; height: 486px; }
  .front__band { position: absolute; left: 0; top: 0; width: 100%; height: 14px; background: var(--ink-deep); }
  .front__brand { position: absolute; left: 0; top: 44px; width: 100%; text-align: center; font-size: 50px; font-weight: 400; letter-spacing: 2px; line-height: 60px; }
  .front__ornament { position: absolute; top: 62px; width: 28px; height: 30px; background: var(--ink); border-radius: 4px; opacity: .85; }
  .front__ornament--left { left: 22px; }
  .front__ornament--right { right: 22px; }
  .front__map { position: absolute; left: 0; top: 124px; width: 100%; height: 224px;
    border-top: 3px solid var(--ink); border-bottom: 3px solid var(--ink);
    background: radial-gradient(ellipse at 55% 45%, var(--map-light) 0%, var(--map-mid) 70%, var(--map-dark) 100%); }
  .front__varietal { position: absolute; left: 147px; top: 298px; width: 190px; height: 94px; background: var(--paper); border: 3px solid var(--ink);
    font-family: "Parisienne", cursive; font-size: 42px; line-height: 88px; text-align: center; color: var(--ink); }
  .front__compass { position: absolute; left: 338px; top: 278px; width: 106px; height: 106px; border-radius: 50%;
    background: radial-gradient(circle, var(--compass-face) 0%, var(--compass-face) 52%, #d8d4c8 56%, var(--compass-rim) 64%, #3a2d20 100%); }
  .front__vintage { position: absolute; left: 0; top: 410px; width: 100%; text-align: center; font-size: 36px; line-height: 40px; }
  .front__region { position: absolute; left: 0; top: 452px; width: 100%; text-align: center; font-size: 17px; font-weight: 700; letter-spacing: 1px; }

  /* Back label */
  .back { left: 655px; top: 269px; width: 425px; height: 424px; text-align: center; }
  .back__brand { position: absolute; left: 0; top: 18px; width: 100%; font-size: 36px; letter-spacing: 1px; }
  .back__rule { position: absolute; left: 166px; width: 88px; }
  .back__rule--top { top: 92px; }
  .back__rule--bottom { top: 164px; }
  .back__vintage { position: absolute; left: 0; top: 106px; width: 100%; font-size: 22px; line-height: 26px; }
  .back__region { position: absolute; left: 0; top: 132px; width: 100%; font-size: 17px; font-weight: 700; letter-spacing: 1px; }
  .back__facts { position: absolute; left: 0; top: 214px; width: 100%; font-size: 11px; font-weight: 700; line-height: 20px; letter-spacing: .5px; }
  .back__warning { position: absolute; left: 28px; top: 284px; width: 369px; font-size: 11px; font-weight: 700; line-height: 13.4px; letter-spacing: .3px; }
  .back__sulfites { position: absolute; left: 0; top: 396px; width: 100%; font-size: 11px; font-weight: 700; letter-spacing: .5px; }
</style>
</head>
<body>
<main class="canvas">

  <section class="label front" aria-label="Front label">
    <div class="front__band"></div>
    <div class="front__ornament front__ornament--left" role="img" aria-label="Fleur-de-lis ornament"></div>
    <h1 class="front__brand">WAYFARERS</h1>
    <div class="front__ornament front__ornament--right" role="img" aria-label="Fleur-de-lis ornament"></div>
    <div class="front__map" role="img" aria-label="Antique map of the world's continents"></div>
    <div class="front__varietal">Zinfandel</div>
    <div class="front__compass" role="img" aria-label="Antique brass compass"></div>
    <p class="front__vintage">2012</p>
    <p class="front__region">SONOMA COUNTRY</p>
  </section>

  <section class="label back" aria-label="Back label">
    <h2 class="back__brand">WAYFARERS</h2>
    <svg class="back__rule back__rule--top" viewBox="0 0 88 8" width="88" height="8" aria-hidden="true">
      <rect x="0" y="0" width="88" height="2.5" fill="var(--ink)"/>
      <rect x="0" y="5.5" width="88" height="2.5" fill="var(--ink)"/>
    </svg>
    <p class="back__vintage">2012</p>
    <p class="back__region">SONOMA COUNTRY</p>
    <svg class="back__rule back__rule--bottom" viewBox="0 0 88 12" width="88" height="12" aria-hidden="true">
      <polygon points="38,5 44,0 50,5" fill="var(--ink)"/>
      <rect x="0" y="4.5" width="88" height="2.5" fill="var(--ink)"/>
      <rect x="0" y="9.5" width="88" height="2.5" fill="var(--ink)"/>
    </svg>
    <p class="back__facts">ALC. 14% VOL. / 750 ML<br>WWW.HOLBROOKWINECO.EXAMPLE</p>
    <p class="back__warning">GOVERNMENT WARNING:<br>(1) ACCORDING TO THE SURGEON GENERAL, WOMEN SHOLD NOT DRINK ALCOHOLIC BEVERAGES DURING PREGNANY BECAUSE OF THE RISK OF BIRTH DEFECTS.<br>(2) CONSUMPTION OF ALCOHOLIC BEVERAGES IMPAIRS YOUR ABILITY TO DRIVE A CAR OR OPERATE MACHINERY, AND MAY CAUSE HEALTH PROBLEMS.</p>
    <p class="back__sulfites">CONTAINS SULFITES</p>
  </section>

</main>
</body>
</html>
```